Business Card Design Project

I need a new business card design for my building/development company: Ridgewell Constructions.

We specialise in small sub-divisions, multi-story developments and new house builds.
We handle the whole process from concept stage right throught to a fully developed property.
Updates

Project Deadline Extended
Reason: Need a couple of extra days to decide as there are so many amazing designs

Target Market(s)

people looking to develop their property and need help. New property buyers

Industry/Entity Type

House

Requirements
Must have
• My logo on both sides:
Side 1: Logo taking up whole side as per old card but with a color/style change.

Side 2: Contact page: include logo but the rest just surprise me!

All contact details will be: (and need to be changable for each employee) I'll inform you of specifics before printing.

Name Surname
Position ie. Managing director
M: insert mobile
E: insert email
P.O. Box 518, Elmhurst, Vic, 3145
www.ridgewellconstructions.com.au

Nice to have
• Colors i'd like: (not necessarily all but this is the basic idea)

Black, blue, grey, silver, white

```html
<!DOCTYPE html>
<html lang="en">
<head>
<meta charset="utf-8">
<title>Ridgewell Constructions – Business Card</title>
<link rel="stylesheet" href="https://fonts.googleapis.com/css2?family=Quicksand:wght@400;500;600;700&display=swap">
<style>
  :root {
    --page-bg: #d9dcdf;
    --card-black: #0d0f11;
    --card-charcoal: #1b1f23;
    --brand-blue: #3ba8e0;
    --brand-blue-dark: #2a8cc4;
    --text-light: #e6e9ec;
    --rule-grey: #8a8f94;
    --paper-white: #ffffff;
    --ghost-blue: #243a48;
  }
  * { box-sizing: border-box; margin: 0; padding: 0; }
  html, body {
    width: 1067px;
    height: 1200px;
    overflow: hidden;
    background: var(--page-bg);
    font-family: "Quicksand", sans-serif;
  }
  .sheet {
    position: relative;
    width: 1067px;
    height: 1200px;
  }
  .card {
    position: absolute;
    left: 203px;
    width: 660px;
    height: 380px;
    border-radius: 4px;
    overflow: hidden;
    background: linear-gradient(135deg, var(--card-charcoal) 0%, var(--card-black) 55%, #15191c 100%);
    box-shadow: 0 12px 30px rgba(0,0,0,0.28);
  }
  .card--front { top: 150px; }
  .card--back { top: 670px; }

  /* Front */
  .front__name {
    position: absolute;
    right: 50px;
    top: 42px;
    font-size: 38px;
    font-weight: 500;
    color: var(--brand-blue);
    letter-spacing: 0.5px;
  }
  .front__role {
    position: absolute;
    right: 50px;
    top: 90px;
    font-size: 14px;
    font-weight: 500;
    color: var(--text-light);
  }
  .front__rule {
    position: absolute;
    left: 24px;
    right: 30px;
    top: 112px;
    height: 2px;
    background: var(--rule-grey);
  }
  .front__contacts {
    position: absolute;
    right: 50px;
    top: 136px;
    text-align: right;
    list-style: none;
    font-size: 19px;
    line-height: 28px;
    font-weight: 500;
    color: var(--text-light);
  }
  .front__contacts .is-link { color: var(--brand-blue); }
  .front__band {
    position: absolute;
    left: 36px;
    right: 22px;
    top: 268px;
    height: 50px;
    border-radius: 25px;
    background: var(--brand-blue);
    color: var(--paper-white);
    font-size: 22px;
    font-weight: 500;
    line-height: 50px;
    padding-left: 340px;
  }
  .front__tile-back {
    position: absolute;
    left: 62px;
    top: 215px;
    width: 170px;
    height: 165px;
    background: var(--brand-blue-dark);
    transform: rotate(-9deg);
  }
  .front__tile {
    position: absolute;
    left: 76px;
    top: 205px;
    width: 160px;
    height: 160px;
    background: var(--paper-white);
    transform: rotate(-3deg);
    display: flex;
    align-items: center;
    justify-content: center;
    text-align: center;
    padding: 12px;
    font-size: 20px;
    font-weight: 700;
    line-height: 24px;
    color: var(--brand-blue);
  }

  /* Back */
  .back__mark {
    position: absolute;
    left: 70px;
    top: 150px;
    font-size: 46px;
    font-weight: 700;
    color: var(--ghost-blue);
    letter-spacing: 0.5px;
    white-space: nowrap;
  }
</style>
</head>
<body>
  <main class="sheet">
    <section class="card card--front" aria-label="Business card front">
      <h1 class="front__name">Name Surname</h1>
      <p class="front__role">Managing director</p>
      <div class="front__rule"></div>
      <ul class="front__contacts">
        <li>P.O. Box 518, Elmhurst, Vic, 3145</li>
        <li>M. phone: 0400 555 218</li>
        <li class="is-link">info@ridgewellconstructions.com.au</li>
        <li class="is-link">www.ridgewellconstructions.com.au</li>
      </ul>
      <div class="front__band">Ridgewell Constructions</div>
      <div class="front__tile-back"></div>
      <div class="front__tile">Ridgewell Constructions</div>
    </section>

    <section class="card card--back" aria-label="Business card back">
      <p class="back__mark">Ridgewell Constructions</p>
    </section>
  </main>
</body>
</html>
```